Adult toys brand needs a Packaging Design

- We need design for packaging for Adult Toys brand.
- Packaging is for vibrators.
- Design needs to be clean and modern, minimal
- Main color is white and purple.
- Brand name is KOVEL, logo is attached.
- Dielines are attached. The packaging consists of the box and the sleeve that goes on the box. We need design for sleeve ONLY.
Updates

Industry/Entity Type

Adult

Font styles to use
Sans Serif

Requirements
Must have
• - Logo
• - item picture (purple version)
• - web address (kovel.example or www.kovel.example)
• - main features

```html
<!DOCTYPE html>
<html lang="en">
<head>
<meta charset="utf-8">
<title>KOVEL sleeve packaging</title>
<link href="https://fonts.googleapis.com/css2?family=Montserrat:wght@400;600;700;800&display=swap" rel="stylesheet">
<style>
  :root {
    --bg: #e9e9eb;
    --sleeve: #fbfbfb;
    --purple: #5a1e5c;
    --purple-light: #8a4a8c;
    --purple-soft: #efe6ef;
    --pink: #e2177e;
    --ink: #3c3c3e;
    --muted: #6a6a6c;
    --gold: #c9a23a;
  }
  * { box-sizing: border-box; margin: 0; padding: 0; }
  html, body { width: 1200px; height: 810px; overflow: hidden; }
  body {
    background: var(--bg);
    font-family: "Montserrat", sans-serif;
    color: var(--ink);
    display: flex;
    align-items: center;
    justify-content: center;
    gap: 70px;
  }
  .panel {
    width: 330px;
    height: 740px;
    background: var(--sleeve);
    box-shadow: 0 10px 30px rgba(0,0,0,.12);
    position: relative;
    overflow: hidden;
  }
  .brand-name {
    font-weight: 800;
    color: var(--ink);
    letter-spacing: 1px;
    line-height: 1;
  }
  .product-image {
    position: absolute;
    background: linear-gradient(160deg, var(--purple-soft) 0%, var(--purple-light) 45%, var(--purple) 100%);
  }

  /* Back panel */
  .back .spec-frame {
    position: absolute;
    left: 36px; right: 36px; top: 40px;
    height: 420px;
    border: 1.5px solid var(--pink);
    padding: 0 24px 20px;
  }
  .back .brand-name {
    display: block;
    width: max-content;
    margin: -15px -8px 14px auto;
    padding: 0 8px;
    font-size: 28px;
    background: var(--sleeve);
  }
  .spec-heading {
    font-size: 12px;
    font-weight: 700;
    color: var(--ink);
    margin: 12px 0 5px;
  }
  .spec-text {
    font-size: 10.5px;
    line-height: 1.35;
    color: var(--muted);
    margin-bottom: 4px;
  }
  .back .product-image {
    left: 0; right: 0; top: 490px;
    height: 190px;
  }
  .back .footer {
    position: absolute;
    left: 36px; right: 36px; bottom: 20px;
    display: flex;
    justify-content: space-between;
    align-items: center;
  }
  .made-in {
    font-size: 10px;
    font-weight: 700;
    color: var(--ink);
  }

  /* Front panel */
  .front .brand-name {
    position: absolute;
    top: 40px; right: 34px;
    font-size: 42px;
  }
  .front .product-image {
    left: 0; right: 0; top: 120px;
    height: 310px;
  }
  .tagline {
    position: absolute;
    right: 34px; top: 455px;
    font-size: 26px;
    font-weight: 800;
    line-height: 1.02;
    color: var(--purple);
    text-align: right;
  }
  .web {
    position: absolute;
    right: 34px; top: 590px;
    font-size: 15px;
    font-weight: 700;
    color: var(--purple);
    letter-spacing: 0.5px;
  }
  .seal {
    position: absolute;
    left: 40px; bottom: 34px;
    width: 64px; height: 64px;
    border-radius: 50%;
    background: var(--gold);
  }
</style>
</head>
<body>

  <section class="panel back" aria-label="Sleeve back panel">
    <div class="spec-frame">
      <span class="brand-name">KOVEL</span>
      <h3 class="spec-heading">Espesicifications</h3>
      <p class="spec-text">Lorem ipsum dolor sit amet, con et sectetur adipiscing elit.</p>
      <p class="spec-text">Curabitur eget mtetus ac turpis viverra consequat.</p>
      <p class="spec-text">Cras ac feet lis blandit nunc semp et er dignissim id vitae enim.</p>
      <h3 class="spec-heading">Instructions</h3>
      <p class="spec-text">Lorem ipsum dolor sit amet, con et sectetur adipiscing elit.</p>
      <p class="spec-text">Curabitur eget mtetus ac turpis viverra consequat.</p>
      <h3 class="spec-heading">More information</h3>
      <p class="spec-text">Lorem ipsum dolor sit amet, con et sectetur adipiscing elit.</p>
      <p class="spec-text">Curabitur eget mtetus ac turpis viverra consequat.</p>
      <p class="spec-text">Cras ac feet lis blandit nunc semp et er dignissim id vitae enim.</p>
    </div>
    <div class="product-image" role="img" aria-label="Photo of the purple vibrator lying diagonally across the panel"></div>
    <div class="footer">
      <svg class="recycle-icons" width="50" height="22" viewBox="0 0 50 22" aria-hidden="true">
        <rect x="3" y="5" width="11" height="14" rx="1" fill="none" stroke="#3c3c3e" stroke-width="2"/>
        <line x1="1" y1="4" x2="16" y2="4" stroke="#3c3c3e" stroke-width="2"/>
        <path d="M30 18 L36 6 L42 18 Z" fill="none" stroke="#3c3c3e" stroke-width="2"/>
      </svg>
      <span class="made-in">Made in country</span>
    </div>
  </section>

  <section class="panel front" aria-label="Sleeve front panel">
    <span class="brand-name">KOVEL</span>
    <div class="product-image" role="img" aria-label="Photo of the purple vibrator with white handle and side arm"></div>
    <p class="tagline">EASY<br>AND<br>SIMPLE</p>
    <p class="web">www.kovel.example</p>
    <div class="seal" role="img" aria-label="Quality seal"></div>
  </section>

</body>
</html>
```